Consulting Company Needs A Trade Show Booth

We are a consulting company in the Pharmaceutical Manufacturing Industry in need of a banner for our trade show booth. The banner design must have a modern look and feel. A template is provided for the trade show booth. Please align your submission with the requirements detailed within the template.
Please see the attached power point file of a concept we mocked-up for the design. The design does not have to match that within the slides. They are only meant to show the elements we need included for design submissions. You can design it to look how you think is best. The theme should match our KVO company color kvo flat.psd (attached). You can look at our web site at www.kvogrp.net to help with ideas and color schemes.
The attached power point includes our older booth designs, as well as some example booths that we liked the feel of. Some pros and cons have been listed to give you an idea of the aspects we like and dislike.
The banner needs to be 10’x8’ with sides as per the banner template attached.
The top of the banner should highlight our company logo (kvo flat.psd), as well as the slogan:
“Enabling Your Company’s Digital Transformation”
In one section of the banner, we would like to highlight our services. This needs to be in the top 2/3 of the banner to remain at eye level.
“Service Offerings”
- MES Consulting
- Software Validation
- Cyber Security
- Operational Intelligence
- System Integration
More on each of the above are on our website: kvogrp.net.
In the other section of the banner, we would like to highlight our mobile apps. This also needs to be in the top 2/3 of the banner to remain at eye level.
“Mobile Apps”
- BinderNova - Bindernova logo-ai.svg
“Quickly Digitize Paper Logbooks and Records”
- vTallyslip – VTS Flat.svg
“Manual Data Entry Into KO”
At the bottom of the banner, we would like to highlight the following partners of ours. Images are attached to this design posting:
- QOR - QOR Partner.png
- ZELTO – Zelto_Logo.png
Also at the bottom of the banner we would like to say:
“30+ Years of Global MES Consulting Experience”.
The attached “Corvel Arc Max 10ft Lightbox.pdf” file gives the exact dimensions necessary and the required directions. Specifically,
* Graphic files need to be built at 72-125 dpi
* Graphic should be created using CMYK and Pantone colors
We have several existing documents to support your design process. Overall, we would like the proposed design to have a simple yet modern look. I have attached the OLD Trade show banners that we have used so that you see what we have used in the past OLD-KVO Banner.png and OLD-KVO Banner 2.png.
Trade Shows
Manufacturing, Life Sciences

```html
<!DOCTYPE html>
<html lang="en">
<head>
<meta charset="utf-8">
<title>KVO Trade Show Banner</title>
<link rel="stylesheet" href="https://fonts.googleapis.com/css2?family=Montserrat:wght@500;600;700;800&family=Open+Sans:wght@700;800&display=swap">
<style>
  :root {
    --brand-blue: #3b78c0;
    --navy: #173768;
    --navy-mid: #1f4a85;
    --sky: #3b80c6;
    --band: #3a7cc4;
    --white: #ffffff;
    --app-text: #2a6bb8;
    --partner-purple: #3d1a6e;
  }
  * { margin: 0; padding: 0; box-sizing: border-box; }
  html, body { width: 1200px; height: 1015px; overflow: hidden; background: var(--white); }
  .banner { position: relative; width: 1200px; height: 1015px; overflow: hidden; font-family: "Montserrat", sans-serif; }
  .banner-shapes { position: absolute; inset: 0; }
  .abs { position: absolute; }

  .brand { left: 69px; top: 70px; display: flex; align-items: center; gap: 16px; }
  .brand-mark { width: 74px; height: 74px; border: 6px solid var(--brand-blue); border-radius: 50%; }
  .brand-name { font-family: "Open Sans", sans-serif; font-weight: 800; color: var(--brand-blue); font-size: 34px; line-height: 1.02; letter-spacing: -0.5px; }

  .tagline { left: 681px; top: 58px; color: var(--brand-blue); font-weight: 700; font-size: 35px; line-height: 46px; letter-spacing: 0.3px; }

  .section-title { left: 88px; top: 213px; width: 420px; text-align: center; color: var(--white); font-weight: 700; font-size: 26px; letter-spacing: 1.5px; }

  .service-label { width: 170px; text-align: center; color: var(--white); font-weight: 600; font-size: 21px; line-height: 27px; }

  .experience { left: 62px; top: 784px; color: var(--white); font-weight: 700; font-size: 31px; line-height: 37px; letter-spacing: 0.6px; }

  .apps-title { left: 760px; top: 232px; width: 326px; display: flex; align-items: center; gap: 12px; color: var(--white); font-weight: 600; font-size: 21px; }
  .apps-title::before, .apps-title::after { content: ""; flex: 1; height: 1px; background: rgba(120,190,255,0.7); }

  .app-card { width: 186px; height: 190px; border-radius: 50%; background: var(--white); display: flex; flex-direction: column; align-items: center; justify-content: center; text-align: center; color: var(--app-text); }
  .app-name { font-weight: 800; font-size: 21px; margin-bottom: 8px; }
  .app-desc { font-weight: 600; font-size: 12.5px; line-height: 15px; }
  .app-dot { width: 14px; height: 14px; border-radius: 50%; background: var(--app-text); margin-bottom: 8px; }

  .partners-label { left: 61px; top: 922px; color: var(--brand-blue); font-weight: 500; font-size: 18px; }
  .partner-badge { left: 173px; top: 907px; width: 101px; height: 61px; background: linear-gradient(135deg, #2f7fd0, #8cc4ef); }
  .partner-divider { left: 292px; top: 905px; width: 1px; height: 64px; background: #c9c9c9; }
  .partner-name { left: 307px; top: 920px; color: var(--partner-purple); font-weight: 600; font-size: 30px; letter-spacing: 1px; }
</style>
</head>
<body>
<main class="banner">
  <svg class="banner-shapes" width="1200" height="1015" viewBox="0 0 1200 1015" aria-hidden="true">
    <defs>
      <linearGradient id="field" x1="0" y1="0" x2="1" y2="0">
        <stop offset="0" stop-color="#173768"/>
        <stop offset="0.55" stop-color="#1f4a85"/>
        <stop offset="1" stop-color="#3b80c6"/>
      </linearGradient>
      <linearGradient id="ribbon" x1="0" y1="0" x2="0" y2="1">
        <stop offset="0" stop-color="#2f68b3"/>
        <stop offset="1" stop-color="#1e4c8c"/>
      </linearGradient>
      <linearGradient id="photo" x1="0" y1="0" x2="0.6" y2="1">
        <stop offset="0" stop-color="#c9cbcf"/>
        <stop offset="0.55" stop-color="#9aa0a8"/>
        <stop offset="1" stop-color="#5b606a"/>
      </linearGradient>
      <path id="hex" d="M0 -43 L37.2 -21.5 L37.2 21.5 L0 43 L-37.2 21.5 L-37.2 -21.5 Z"/>
      <path id="hex-in" d="M0 -36 L31.2 -18 L31.2 18 L0 36 L-31.2 18 L-31.2 -18 Z"/>
    </defs>

    <!-- blue field -->
    <path d="M0 244 L560 244 Q578 244 590 230 L628 188 Q640 176 658 176 L1200 176 L1200 870 L0 870 Z" fill="url(#field)"/>
    <rect x="0" y="770" width="701" height="100" fill="var(--band)"/>

    <!-- ribbon -->
    <polygon points="72,244 90,209 104,244" fill="#3a78c4"/>
    <polygon points="523,244 505,209 491,244" fill="#3a78c4"/>
    <path d="M86 209 L509 209 L498 252 Q495 262 484 262 L111 262 Q100 262 97 252 Z" fill="url(#ribbon)"/>

    <!-- service icons -->
    <g class="service-icon" transform="translate(127 354)">
      <ellipse cx="0" cy="52" rx="34" ry="4" fill="#0e2347" opacity="0.6"/>
      <use href="#hex" fill="#2f6fc0"/><use href="#hex-in" fill="#fff"/>
      <g fill="none" stroke="#2f6fc0" stroke-width="2">
        <circle cx="-12" cy="-14" r="5"/><circle cx="12" cy="-14" r="5"/>
        <path d="M-20 10 V-4 H-6 M20 10 V-4 H6 M-10 4 H10 M-4 4 V16 M4 4 V16"/>
      </g>
    </g>
    <g class="service-icon" transform="translate(314 354)">
      <ellipse cx="0" cy="52" rx="34" ry="4" fill="#0e2347" opacity="0.6"/>
      <use href="#hex" fill="#2f6fc0"/><use href="#hex-in" fill="#fff"/>
      <g fill="none" stroke="#2f6fc0" stroke-width="2.5">
        <circle cx="0" cy="0" r="17"/><path d="M-8 0 L-2 7 L10 -7"/><path d="M12 12 L20 20"/>
      </g>
    </g>
    <g class="service-icon" transform="translate(481 354)">
      <ellipse cx="0" cy="52" rx="34" ry="4" fill="#0e2347" opacity="0.6"/>
      <use href="#hex" fill="#2f6fc0"/><use href="#hex-in" fill="#fff"/>
      <g fill="none" stroke="#2f6fc0" stroke-width="2">
        <path d="M0 -18 L15 -12 V2 Q15 14 0 20 Q-15 14 -15 2 V-12 Z"/>
        <rect x="-6" y="-2" width="12" height="10"/><path d="M-4 -2 V-6 A4 4 0 0 1 4 -6 V-2"/>
      </g>
    </g>
    <g class="service-icon" transform="translate(127 548)">
      <ellipse cx="0" cy="52" rx="34" ry="4" fill="#0e2347" opacity="0.6"/>
      <use href="#hex" fill="#2f6fc0"/><use href="#hex-in" fill="#fff"/>
      <g fill="none" stroke="#2f6fc0" stroke-width="2">
        <rect x="-11" y="-11" width="22" height="22"/><circle cx="0" cy="0" r="5"/>
        <path d="M-11 -5 H-20 M-11 5 H-20 M11 -5 H20 M11 5 H20 M-5 -11 V-20 M5 -11 V-20 M-5 11 V20 M5 11 V20"/>
      </g>
    </g>
    <g class="service-icon" transform="translate(314 548)">
      <ellipse cx="0" cy="52" rx="34" ry="4" fill="#0e2347" opacity="0.6"/>
      <use href="#hex" fill="#2f6fc0"/><use href="#hex-in" fill="#fff"/>
      <g fill="none" stroke="#2f6fc0" stroke-width="2">
        <rect x="-20" y="-15" width="40" height="26"/><path d="M-6 11 V17 M6 11 V17 M-10 17 H10"/>
        <path d="M-14 2 L-6 -6 L2 0 L12 -10"/>
      </g>
    </g>

    <!-- hex photo frame -->
    <polygon points="930,532 1169,670 1169,946 930,1084 691,946 691,670" fill="none" stroke="#fff" stroke-width="4"/>
    <polygon points="930,543 1160,676 1160,941 930,1074 700,941 700,676" fill="#2b64b0"/>
    <polygon points="930,556 1149,683 1149,934 930,1061 711,934 711,683" fill="#fff"/>
  </svg>

  <svg class="abs" style="left:0;top:0" width="1200" height="1015" viewBox="0 0 1200 1015" role="img" aria-label="Photo of hands typing on a laptop with glowing digital checkmark and network icons">
    <polygon points="930,569 1137,689 1137,928 930,1048 723,928 723,689" fill="url(#photo)" stroke="url(#photo)" stroke-width="14" stroke-linejoin="round"/>
  </svg>

  <div class="abs brand">
    <span class="brand-mark"></span>
    <span class="brand-name">kinetic value<br>operations</span>
  </div>

  <h1 class="abs tagline">Enabling Your Company’s<br>Digital Transformation</h1>

  <h2 class="abs section-title">SERVICE OFFERINGS</h2>
  <p class="abs service-label" style="left:42px;top:412px">MES<br>Consulting</p>
  <p class="abs service-label" style="left:229px;top:412px">Software<br>Validation</p>
  <p class="abs service-label" style="left:396px;top:412px">Cyber<br>Security</p>
  <p class="abs service-label" style="left:42px;top:606px">System<br>Integration</p>
  <p class="abs service-label" style="left:209px;top:606px;width:210px">Operational<br>Intelligence</p>

  <h2 class="abs apps-title">Mobile Apps</h2>
  <div class="abs app-card" style="left:730px;top:285px">
    <span class="app-dot"></span>
    <span class="app-name">BinderNova</span>
    <span class="app-desc">Quickly Digitize<br>Paper Logbooks<br>and Records</span>
  </div>
  <div class="abs app-card" style="left:931px;top:285px">
    <span class="app-dot"></span>
    <span class="app-name">vTallyslip</span>
    <span class="app-desc">Manual<br>Data Entry<br>into a Historian</span>
  </div>

  <p class="abs experience">30+ YEARS OF GLOBAL<br>MES CONSULTING EXPERIENCE</p>

  <p class="abs partners-label">Partners</p>
  <div class="abs partner-badge" role="img" aria-label="Partner badge"></div>
  <span class="abs partner-divider"></span>
  <p class="abs partner-name">ZELTO</p>
</main>
</body>
</html>
```